Marlow Cat Lodge needs a website and a logo :)

I need a web design for my pet hotel. I will use it in Wordpress, probable with Elementor, so if you can also offer the WP template creation, that's a bonus but I don't wanna book the coded-website option here as I don't think that applies to WP. It would be great if you come up with a logo as well.

Here some info:

Modern, premium cat boarding with a vet on-site

Marlow Cat Lodge is a boutique cat boarding facility in Nelson, New Zealand, offering high-quality, vet-supervised care for all cats, including those with special medical needs. Unlike standard catteries, we focus on low-stress boarding, with separate spaces for special-needs and healthy cats, ensuring a safe, comfortable, and peaceful environment. We also prioritize convenience with self check-in and check-out, leveraging technology to enhance the experience.

Target Market(s)

Cat owners for short term to long term stays that don't want the cheapest option and will value that we have a vet on-site

Industry/Entity Type

cat boarding

Number of Pages Required

5+ page

Font styles to use
Sans Serif
Other font styles liked:
• Nothing that needs installation or a license. Please use Google Fonts.

Requirements
Must have
• Landing page, about us, services, blog and contact page - the landing page should have the typical sales layout with hero image top right, a tag line "Modern, premium cat boarding with a vet on-site" and 2 paragraphs. Paragraph 1 (Problem): Leaving your cat behind can be stressful, especially if they need special care. Standard catteries often lack vet oversight and a calm, tailored environment. Paragraph 2 (Solution): At Marlow Cat Lodge, we offer premium, vet-supervised boarding with separate spaces for special-needs and healthy cats. Our self check-in and tech-driven system makes drop-offs and pick-ups effortless... you know the drill :)
Nice to have
• Ask ChatGPT for some ideas and give it the business plan: https://files.example-docs.net/document/d/7qerTy_LKMWBP2hfsx8V304UiLoXyOpqRkZjTnWaBcD/edit?usp=sharing
Should not have
• NO DOGS :)

```html
<!DOCTYPE html>
<html lang="en">
<head>
<meta charset="utf-8">
<title>Marlow Cat Lodge</title>
<link href="https://fonts.googleapis.com/css2?family=Josefin+Sans:wght@400;600;700&display=swap" rel="stylesheet">
<style>
:root{
  --orange:#ee7a22;
  --orange-soft:#fbe3cf;
  --ink:#141414;
  --muted:#555;
  --cream:#fcf7f1;
  --lilac:#f8f6fc;
  --line:#eee6de;
  --backdrop:#a3a3a3;
  --white:#fff;
}
*{box-sizing:border-box;margin:0;padding:0}
html,body{width:1200px;height:3131px;overflow:hidden;background:var(--backdrop);font-family:"Josefin Sans",sans-serif;color:var(--ink)}
.page{position:absolute;left:119px;top:112px;width:962px;height:2908px;background:var(--white);overflow:hidden}
.abs{position:absolute}
.brand{font-size:17px;font-weight:600;color:var(--orange);display:flex;align-items:center;gap:6px}
.brand i{width:12px;height:12px;background:var(--orange);border-radius:50%;display:block}
.nav a{position:absolute;top:22px;font-size:9px;font-weight:600;color:var(--ink);text-decoration:none}
.nav a.on{color:var(--orange)}
.cart{left:749px;top:11px;width:58px;height:22px;border:1px solid var(--orange);border-radius:3px;font-size:8px;font-weight:600;display:flex;align-items:center;justify-content:center;gap:3px}
.hero-bg{left:0;top:46px;width:962px;height:470px;background:var(--cream)}
h1{font-size:30px;font-weight:700;line-height:40px;text-align:center;width:962px;left:0;top:105px}
.lead{left:331px;top:192px;width:300px;text-align:center;font-size:8px;line-height:13px;color:var(--muted)}
.btn{background:var(--orange);color:var(--white);font-weight:600;display:flex;align-items:center;justify-content:center;border-radius:3px}
.feat{width:126px;height:57px;background:var(--white);border-radius:4px;font-size:10px;font-weight:600;display:flex;align-items:flex-end;justify-content:center;padding-bottom:14px}
.feat-ic{width:28px;height:28px;border-radius:50%;background:var(--orange-soft);border:3px solid var(--white)}
.photo{border-radius:3px}
.eyebrow{font-size:8px;font-weight:700;color:var(--orange);text-transform:uppercase}
.center{left:0;width:962px;text-align:center}
h2{font-size:26px;font-weight:700}
.svc{width:207px;height:124px;border:1px solid var(--line);border-radius:4px;padding:24px 17px}
.svc h3{font-size:10px;font-weight:600;display:flex;align-items:center;gap:8px;margin-bottom:9px}
.svc h3 span{width:22px;height:18px;border:1.5px solid var(--orange);border-radius:3px;display:block}
.svc p{font-size:8px;line-height:12px;color:var(--muted)}
.svc a{display:block;margin-top:7px;font-size:9px;font-weight:700;color:var(--orange);text-decoration:none}
.acc{left:155px;width:262px;border-bottom:1px solid var(--line);padding-bottom:14px}
.acc h4{font-size:9px;font-weight:600;display:flex;justify-content:space-between;align-items:center}
.acc h4 b{width:18px;height:18px;background:var(--orange);border-radius:3px;color:var(--white);font-size:9px;display:flex;align-items:center;justify-content:center}
.acc p{font-size:8px;line-height:11px;color:var(--muted);margin-top:6px;width:235px}
.tile{width:207px;height:207px}
.plan{width:207px;height:312px;border:1px solid var(--line);background:var(--white);border-radius:3px;padding:22px 18px;text-align:center}
.plan h3{font-size:19px;font-weight:700}
.plan .sub{font-size:10px;color:var(--muted);margin-top:3px}
.plan .desc{font-size:7.5px;line-height:10px;color:var(--muted);margin:16px auto 0;width:170px;height:40px}
.plan ul{list-style:none;text-align:left;margin-top:8px}
.plan li{font-size:8px;color:var(--muted);height:25px;display:flex;align-items:center;gap:7px}
.plan li:before{content:"✓";width:10px;height:10px;border-radius:50%;background:var(--orange);color:var(--white);font-size:7px;display:flex;align-items:center;justify-content:center}
.plan .btn{position:absolute;left:18px;bottom:20px;width:171px;height:44px;font-size:14px;border-radius:2px}
.plan.hot{background:var(--orange);border-color:var(--orange);color:var(--white)}
.plan.hot .sub,.plan.hot .desc,.plan.hot li{color:var(--white)}
.plan.hot li:before{background:var(--white);color:var(--orange)}
.plan.hot .btn{background:var(--white);color:var(--orange)}
.quote{width:215px;height:128px;background:var(--white);border-radius:4px;padding:16px 15px}
.quote .who{display:flex;align-items:center;gap:10px}
.quote .av{width:32px;height:32px;border-radius:50%;background:linear-gradient(135deg,#8a8078,#d8d0c6)}
.quote b{font-size:11px;display:block}
.quote small{font-size:8px;font-weight:600}
.quote .mark{position:absolute;right:15px;top:14px;font-size:40px;line-height:40px;color:var(--orange);font-weight:700}
.quote .stars{color:#f5b400;font-size:9px;margin-top:10px;letter-spacing:1px}
.quote p{font-size:8px;line-height:11px;color:var(--muted);margin-top:4px}
.foot h5{font-size:11px;font-weight:600}
.foot p,.foot li{font-size:8px;line-height:14px;color:var(--muted)}
.hours{left:341px;top:2765px;width:150px;height:70px;background:var(--cream);padding:10px 12px;font-size:8px;color:var(--muted)}
.hours div{display:flex;justify-content:space-between;height:17px}
.links ul{list-style:none}
.links li:before{content:"• ";color:var(--orange)}
.copy{left:0;width:962px;top:2885px;text-align:center;font-size:7.5px;color:var(--ink)}
</style>
</head>
<body>
<div class="page">

  <!-- Header -->
  <div class="abs brand" style="left:155px;top:13px"><i></i>Marlow Cat Lodge</div>
  <nav class="nav">
    <a class="on" style="left:338px">Home ⌄</a>
    <a style="left:402px">Services ⌄</a>
    <a style="left:474px">Shop ⌄</a>
    <a style="left:535px">Blog ⌄</a>
    <a style="left:593px">Pages ⌄</a>
  </nav>
  <div class="abs cart"><span style="color:var(--orange)">●</span>2 item</div>

  <!-- Hero -->
  <div class="abs hero-bg"></div>
  <svg class="abs" style="left:0;top:420px" width="962" height="100" viewBox="0 0 962 100">
    <path d="M0 30 Q240 110 480 50 T962 40 V100 H0Z" fill="#fff"/>
    <path d="M40 82 Q240 110 480 50 T860 40" fill="none" stroke="#f3b890" stroke-width="2" stroke-dasharray="60 25"/>
  </svg>
  <div class="abs" style="left:85px;top:205px;width:136px;height:136px;border-radius:50%;background:var(--orange)"></div>
  <div class="abs" style="left:74px;top:194px;width:158px;height:158px;border-radius:50%;border:2px solid var(--orange);clip-path:inset(0 0 60% 0)"></div>
  <div class="abs" role="img" aria-label="Tabby cat leaping" style="left:32px;top:225px;width:175px;height:235px;border-radius:40% 30% 35% 45%;background:linear-gradient(150deg,#b39a7e,#6d5a47)"></div>
  <div class="abs" style="left:696px;top:183px;width:170px;height:170px;border-radius:50%;background:var(--orange)"></div>
  <div class="abs" role="img" aria-label="Fluffy calico cat sitting" style="left:710px;top:135px;width:252px;height:250px;border-radius:45% 40% 20% 40%;background:linear-gradient(160deg,#e9e3dc,#9e9188)"></div>
  <div class="abs" style="left:84px;top:133px;width:9px;height:9px;border-radius:50%;background:#8e93ad"></div>
  <div class="abs" style="left:267px;top:216px;width:9px;height:9px;border-radius:50%;background:#8e93ad"></div>
  <div class="abs" style="left:873px;top:172px;width:13px;height:13px;border-radius:50%;background:#c9c9c9"></div>
  <div class="abs" style="left:758px;top:98px;width:9px;height:9px;border-radius:50%;background:#c9c9c9"></div>
  <div class="abs" style="left:214px;top:162px;width:4px;height:4px;border-radius:50%;background:var(--orange)"></div>

  <h1 class="abs">Modern, Premium Cat<br>Boarding with a Vet On-Site</h1>
  <p class="abs lead">Luxury cat accommodation in Nelson, NZ – designed for comfort, health, and peace of mind.</p>
  <div class="abs btn" style="left:433px;top:233px;width:95px;height:33px;font-size:9px">● Our Service</div>

  <div class="abs feat" style="left:277px;top:321px">Vet Services</div>
  <div class="abs feat" style="left:418px;top:321px">Special Care</div>
  <div class="abs feat" style="left:559px;top:321px">High Quality</div>
  <div class="abs feat-ic" style="left:326px;top:305px"></div>
  <div class="abs feat-ic" style="left:467px;top:305px"></div>
  <div class="abs feat-ic" style="left:608px;top:305px"></div>

  <!-- Services -->
  <div class="abs eyebrow center" style="top:570px">Our Services</div>
  <h2 class="abs center" style="top:585px">All Care Services</h2>
  <div class="abs svc" style="left:155px;top:621px"><h3><span></span>Luxury Environment</h3><p>Lorem ipsum dolor sit amet, consectetuer adipiscing elit, sed diam nonummy.</p><a>Get Service →</a></div>
  <div class="abs svc" style="left:378px;top:621px"><h3><span></span>Vet On-Site</h3><p>Lorem ipsum dolor sit amet, consectetuer adipiscing elit, sed diam nonummy.</p><a>Get Service →</a></div>
  <div class="abs svc" style="left:599px;top:621px"><h3><span></span>Tech-Driven Updates</h3><p>Lorem ipsum dolor sit amet, consectetuer adipiscing elit, sed diam nonummy.</p><a>Get Service →</a></div>
  <div class="abs svc" style="left:155px;top:760px"><h3><span></span>Luxury Environment</h3><p>Lorem ipsum dolor sit amet, consectetuer adipiscing elit, sed diam nonummy.</p><a>Get Service →</a></div>
  <div class="abs svc" style="left:378px;top:760px"><h3><span></span>Vet On-Site</h3><p>Lorem ipsum dolor sit amet, consectetuer adipiscing elit, sed diam nonummy.</p><a>Get Service →</a></div>
  <div class="abs svc" style="left:599px;top:760px"><h3><span></span>Tech-Driven Updates</h3><p>Lorem ipsum dolor sit amet, consectetuer adipiscing elit, sed diam nonummy.</p><a>Get Service →</a></div>

  <!-- Why choose us -->
  <div class="abs eyebrow" style="left:155px;top:977px">Why Choose Us?</div>
  <h2 class="abs" style="left:155px;top:990px;line-height:29px;font-size:25px">Leaving Your Cat Behind<br>Shouldn’t Be Stressful</h2>
  <div class="abs acc" style="top:1073px"><h4 style="color:var(--orange)">Problem Paragraph:<b>⌃</b></h4><p>Many catteries lack vet supervision and a calm, tailored environment. If your cat has medical needs, finding safe, specialized care can be challenging.</p></div>
  <div class="abs acc" style="top:1150px"><h4>Solution Paragraph:<b>⌄</b></h4></div>
  <div class="abs acc" style="top:1194px;border:0"><h4>Visuals:<b>⌄</b></h4></div>
  <div class="abs" style="left:718px;top:955px;width:175px;height:175px;border-radius:50%;background:var(--orange)"></div>
  <div class="abs" style="left:705px;top:942px;width:201px;height:201px;border-radius:50%;border:2px solid var(--orange);clip-path:inset(0 0 0 60%)"></div>
  <div class="abs photo" role="img" aria-label="Vet checking a cat in a boarding suite" style="left:474px;top:977px;width:230px;height:221px;background:linear-gradient(135deg,#f1eee9,#c9c2b6)"></div>
  <div class="abs photo" role="img" aria-label="Row of cat boarding suites" style="left:655px;top:1050px;width:112px;height:98px;border:3px solid #fff;background:linear-gradient(135deg,#e6e4e0,#a9a49d)"></div>
  <div class="abs photo" role="img" aria-label="White cattery cabinets" style="left:590px;top:1117px;width:143px;height:126px;border:3px solid #fff;background:linear-gradient(135deg,#f2f0ec,#bdb8b0)"></div>

  <!-- Gallery -->
  <div class="abs eyebrow center" style="top:1305px">Favorite Cats</div>
  <h2 class="abs center" style="top:1320px">Our Gallery</h2>
  <div class="abs tile" role="img" aria-label="Two cats nuzzling outdoors" style="left:155px;top:1355px;background:linear-gradient(135deg,#6f7a5c,#e2b68a)"></div>
  <div class="abs tile" role="img" aria-label="Ginger cat being brushed" style="left:378px;top:1355px;background:linear-gradient(135deg,#c8773a,#8a4d22)">
    <div style="position:absolute;top:100px;width:100%;text-align:center;color:#fff;font-size:14px;font-weight:600">German Cat</div>
    <div style="position:absolute;left:71px;top:150px;width:66px;height:21px;background:#fff;color:var(--orange);font-size:9px;font-weight:600;display:flex;align-items:center;justify-content:center;border-radius:2px">More</div>
  </div>
  <div class="abs tile" role="img" aria-label="Two Siamese cats being held" style="left:599px;top:1355px;background:linear-gradient(135deg,#4a3c33,#e8ddd0)"></div>
  <div class="abs tile" role="img" aria-label="Calico cat lying on a step" style="left:155px;top:1576px;background:linear-gradient(135deg,#8a6c5f,#d9d2c8)"></div>
  <div class="abs tile" role="img" aria-label="Tabby kitten looking up" style="left:378px;top:1576px;background:linear-gradient(135deg,#7a8a96,#d2c4ad)"></div>
  <div class="abs tile" role="img" aria-label="Fluffy white kitten by a door" style="left:599px;top:1576px;background:linear-gradient(135deg,#e8e4de,#2b2623)"></div>

  <!-- Pricing -->
  <div class="abs" style="left:0;top:1841px;width:962px;height:480px;background:var(--lilac)"></div>
  <div class="abs eyebrow center" style="top:1887px">Our Services</div>
  <h2 class="abs center" style="top:1901px">All Care Services</h2>
  <p class="abs" style="left:341px;top:1935px;width:280px;text-align:center;font-size:8px;line-height:13px;color:var(--muted)">Each service should have: a title, short description, price range (if applicable), and an icon or image.</p>
  <div class="abs plan" style="left:155px;top:1970px">
    <h3>Standard Boarding</h3><div class="sub">(For Healthy Cats)</div>
    <p class="desc">The perfect stay for your feline friend in a quiet, luxurious environment.</p>
    <ul><li>Private, spacious cat suites</li><li>Daily playtime &amp; socialization</li><li>Premium cat food or bring your own</li><li>Regular updates via our app</li><li>Pricing: $X per night</li></ul>
    <div class="btn">Purchase Now</div>
  </div>
  <div class="abs plan hot" style="left:378px;top:1970px">
    <h3>Medical Boarding</h3><div class="sub">(For Cats with Special Needs)</div>
    <p class="desc">Supervised by our on-site vet, ideal for senior cats or those requiring medication.</p>
    <ul><li>Care tailored to medical conditions</li><li>Medication administration</li><li>Daily vet check-ins</li><li>Low-stress environment</li><li>Pricing: Custom quote</li></ul>
    <div class="btn">Purchase Now</div>
  </div>
  <div class="abs plan" style="left:599px;top:1970px">
    <h3>Luxury Upgrades</h3><div class="sub">(Optional Add-Ons)</div>
    <p class="desc">Pamper your cat with additional services.</p>
    <ul><li>Extra cuddle &amp; playtime – $40</li><li>Video updates for owners – $60</li><li>Gourmet meal plan – $80</li><li>Basic grooming – $100</li></ul>
    <div class="btn">Purchase Now</div>
  </div>

  <!-- Testimonials -->
  <div class="abs" style="left:0;top:2321px;width:962px;height:362px;background:var(--cream)"></div>
  <svg class="abs" style="left:0;top:2300px" width="962" height="60" viewBox="0 0 962 60">
    <path d="M0 0 H962 V30 Q700 0 480 40 T0 20Z" fill="var(--lilac)"/>
    <path d="M10 30 Q240 60 480 40" fill="none" stroke="#f3b890" stroke-width="2" stroke-dasharray="60 25"/>
  </svg>
  <div class="abs photo" role="img" aria-label="Two cats cuddling" style="left:612px;top:2318px;width:195px;height:145px;background:linear-gradient(135deg,#7b8066,#e3b888)"></div>
  <div class="abs eyebrow" style="left:155px;top:2439px">Testimonials</div>
  <h2 class="abs" style="left:155px;top:2455px;font-size:25px">What People Say</h2>
  <div class="abs quote" style="left:-75px;top:2513px"><div class="who"><span class="av"></span><div><b>Across Nelson</b><small>Lorem ipsum</small></div></div><span class="mark">”</span><div class="stars">★★★★★</div><p>Lorem ipsum dolor sit amet, consectetuer adipiscing elit, sed diam nonummy nibh euismod tincidunt.</p></div>
  <div class="abs quote" style="left:155px;top:2513px"><div class="who"><span class="av"></span><div><b>Across Nelson</b><small>Lorem ipsum</small></div></div><span class="mark">”</span><div class="stars">★★★★★</div><p>Lorem ipsum dolor sit amet, consectetuer adipiscing elit, sed diam nonummy nibh euismod tincidunt.</p></div>
  <div class="abs quote" style="left:385px;top:2513px"><div class="who"><span class="av"></span><div><b>Across Nelson</b><small>Lorem ipsum</small></div></div><span class="mark">”</span><div class="stars">★★★★★</div><p>Lorem ipsum dolor sit amet, consectetuer adipiscing elit, sed diam nonummy nibh euismod tincidunt.</p></div>
  <div class="abs quote" style="left:615px;top:2513px"><div class="who"><span class="av"></span><div><b>Across Nelson</b><small>Lorem ipsum</small></div></div><span class="mark">”</span><div class="stars">★★★★★</div><p>Lorem ipsum dolor sit amet, consectetuer adipiscing elit, sed diam nonummy nibh euismod tincidunt.</p></div>
  <div class="abs quote" style="left:845px;top:2513px"><div class="who"><span class="av"></span><div><b>Across Nelson</b><small>Lorem ipsum</small></div></div><span class="mark">”</span><div class="stars">★★★★★</div><p>Lorem ipsum dolor sit amet, consectetuer adipiscing elit, sed diam nonummy nibh euismod tincidunt.</p></div>

  <!-- Footer -->
  <footer class="foot">
    <div class="abs brand" style="left:155px;top:2722px"><i></i>Marlow Cat Lodge</div>
    <p class="abs" style="left:155px;top:2766px;width:135px">Lorem ipsum dolor sit amet, consectetuer adipiscing elit, sed diam nonummy nibh euismod tincidunt.</p>
    <h5 class="abs" style="left:341px;top:2733px">Working Hours</h5>
    <div class="abs hours">
      <div><span>Mon - Fri:</span><span>7am - 6pm</span></div>
      <div><span>Saturday</span><span>9am - 4pm</span></div>
      <div><span>Sunday</span><span style="color:var(--orange)">Closed</span></div>
    </div>
    <h5 class="abs" style="left:525px;top:2733px">Useful Links</h5>
    <div class="abs links" style="left:525px;top:2760px"><ul><li>Home</li><li>About</li><li>Services</li><li>Shop</li></ul></div>
    <div class="abs links" style="left:578px;top:2760px"><ul><li>FAQ</li><li>Gallery</li><li>Delivery</li><li>Sales</li></ul></div>
    <h5 class="abs" style="left:640px;top:2733px">Newsletter</h5>
    <p class="abs" style="left:640px;top:2760px;width:170px">Lorem ipsum dolor sit amet, consectetuer adipiscing elit.</p>
    <div class="abs" style="left:640px;top:2795px;width:140px;height:22px;border:1px solid #ddd;border-radius:2px;font-size:8px;color:#999;padding:7px 10px">Email</div>
    <div class="abs btn" style="left:785px;top:2795px;width:22px;height:22px;font-size:10px">→</div>
    <div class="abs" style="left:155px;top:2866px;width:652px;height:1px;background:var(--line)"></div>
    <p class="abs copy">© Copyright 2025 | Harbour Vale Veterinary Clinics | All Rights Reserved | Privacy Policy | Terms and Conditions | Find Vet Jobs</p>
  </footer>
</div>
</body>
</html>
```